Kids Bamboo sun protection clothing

We need a flyer to promote our bamboo sun protection range to parents of kids with sensitive due to illness or skin conditions.
Our clothing is made from bamboo that has been specially knitted for high sun protection but does not use chemicals. The clothing is for everyday wear, to the playground, going for walks, after a swim. Special features such as hoods, high necklines, long sleeves and thumb loops create more coverage but it is not a lycra rash vest. You can see the product at www.lumora-wear.com. We would like this flyer (or postcard) to show parents with children who are sensitive tot he sun that there is an option. Their kids might have albinism, Cancer or severe burns, might be sensitive to the sun or have Eczema. These clothes are natural fabric with styling to help look after their skin in the sun. We would like a soft caring approach.

Target Market(s)

Mums of children who have sensitive skin due to burns, cancer, Eczema or UV sensitivity.

Industry/Entity Type

Health

Font styles to use
Sans Serif

Requirements
Must have
• Point out how it can protect the skin with fabric and design features.
• Be eye catching so if it is in a waiting room at the doctors people will go over to pick it up. Be a soft approach that does not concentrate on the illness.
• Website details
Nice to have
• mention that we also do women's wear
• Please use any images off the website

```html
<!DOCTYPE html>
<html lang="en">
<head>
<meta charset="utf-8">
<title>Lumora Kids Clothing – Flyer</title>
<link href="https://fonts.googleapis.com/css2?family=Arimo:wght@400;700&family=Lato:wght@400&family=Roboto+Condensed:wght@700&display=swap" rel="stylesheet">
<style>
  :root{
    --orange:#f9a93a;
    --grey:#6d6e71;
    --ink:#1e1e1e;
    --text-grey:#4b4b4d;
    --sky:#7fa3e2;
    --sky-deep:#6f95dc;
    --sky-light:#a9c3f0;
    --sand:#e2c9a4;
    --white:#ffffff;
  }
  *{box-sizing:border-box;margin:0;padding:0}
  html,body{width:1200px;height:1200px;overflow:hidden;background:var(--white)}
  body{position:relative;font-family:"Arimo",Arial,sans-serif;color:var(--ink)}
  .card{position:absolute;background:var(--white);overflow:hidden;box-shadow:0 4px 12px rgba(0,0,0,.28)}
  .card--front{left:218px;top:42px;width:764px;height:545px}
  .card--back{left:218px;top:610px;width:768px;height:547px}
  .card__art{position:absolute;left:0;top:0}
  .footer{position:absolute;left:0;bottom:0;width:100%;height:33px;background:var(--grey);
    color:var(--white);font-size:16px;letter-spacing:4.5px;text-align:center;line-height:33px}

  .brand{position:absolute;left:333px;top:127px;width:208px;text-align:center;
    font-family:"Arimo",sans-serif;font-weight:400;font-size:34px;letter-spacing:3px;color:var(--grey)}
  .headline{position:absolute;left:453px;top:262px;line-height:1;font-weight:400}
  .headline__name{display:block;font-family:"Roboto Condensed",sans-serif;font-weight:700;font-size:48px;color:var(--orange)}
  .headline__sub{display:block;font-family:"Arimo",sans-serif;font-weight:400;font-size:44px;color:var(--text-grey);margin-top:2px}
  .needs{position:absolute;left:453px;top:369px;list-style:none;font-family:"Lato",sans-serif;font-size:14.5px;color:var(--ink)}
  .needs li{position:relative;padding-left:14px;margin-bottom:8px;line-height:18px}
  .needs li::before{content:"";position:absolute;left:0;top:7px;width:6px;height:6px;border-radius:50%;background:var(--orange)}
  .intro{position:absolute;left:22px;top:434px;width:330px;font-size:16px;line-height:21.5px}

  .features-title{position:absolute;right:16px;top:20px;font-size:46px;font-weight:400;color:var(--orange);line-height:1}
  .feature{position:absolute;height:35px;background:var(--grey);color:var(--white);font-size:16px;line-height:35px;
    box-shadow:0 8px 8px -6px rgba(0,0,0,.18)}
  .feature--necklines{left:546px;top:80px;width:222px;padding-left:32px}
  .feature--sleeves{left:430px;top:192px;width:192px;border-radius:8px 0 0 8px;padding-left:45px}
  .feature--loops{left:514px;top:299px;width:254px;padding-left:38px}
  .feature--fabrics{left:430px;top:421px;width:216px;border-radius:8px 0 0 8px;padding-left:44px}
  .testing{position:absolute;left:22px;top:433px;width:300px;font-size:12.3px;line-height:15.3px}
  .testing__link{color:var(--orange)}
</style>
</head>
<body>

<section class="card card--front">
  <svg class="card__art" width="764" height="545" viewBox="0 0 764 545">
    <defs>
      <linearGradient id="frontScene" x1="0" y1="0" x2="0" y2="1">
        <stop offset="0" stop-color="var(--sky)"/>
        <stop offset=".78" stop-color="var(--sky-deep)"/>
        <stop offset=".9" stop-color="#c9c0c4"/>
        <stop offset="1" stop-color="var(--sand)"/>
      </linearGradient>
      <linearGradient id="frontFade" x1="0" y1="0" x2="1" y2="0">
        <stop offset="0" stop-color="#ffffff" stop-opacity="0"/>
        <stop offset=".62" stop-color="#ffffff" stop-opacity=".15"/>
        <stop offset=".86" stop-color="#ffffff" stop-opacity=".85"/>
        <stop offset="1" stop-color="#ffffff"/>
      </linearGradient>
      <linearGradient id="playScene" x1="0" y1="0" x2="0" y2="1">
        <stop offset="0" stop-color="var(--sky)"/>
        <stop offset=".6" stop-color="var(--sky-deep)"/>
        <stop offset=".8" stop-color="#b9a6c9"/>
        <stop offset="1" stop-color="var(--sand)"/>
      </linearGradient>
      <clipPath id="heroClip"><circle cx="640" cy="118" r="92"/></clipPath>
    </defs>
    <g role="img" aria-label="Children in bamboo sun clothing playing with balloons on sand">
      <path d="M0 0 H430 V236 C300 352 150 398 0 370 Z" fill="url(#frontScene)"/>
      <path d="M0 0 H430 V236 C300 352 150 398 0 370 Z" fill="url(#frontFade)"/>
    </g>
    <path d="M-5 370 C150 398 300 352 430 236" fill="none" stroke="var(--orange)" stroke-width="15"/>
    <path d="M-5 392 C170 418 332 362 446 256" fill="none" stroke="var(--grey)" stroke-width="5"/>

    <path d="M590 0 H764 V42 C720 26 672 24 630 34 Z" fill="var(--orange)"/>
    <path d="M700 56 C728 50 748 49 764 49 V82 C748 82 730 84 712 90 Z" fill="var(--grey)"/>

    <circle cx="437" cy="142" r="108" fill="none" stroke="var(--grey)" stroke-width="3"/>
    <circle cx="437" cy="142" r="102" fill="var(--white)" stroke="var(--orange)" stroke-width="6"/>

    <g role="img" aria-label="Two girls playing in the sand wearing sun protective clothing" clip-path="url(#heroClip)">
      <rect x="540" y="20" width="200" height="200" fill="url(#playScene)"/>
    </g>
    <circle cx="640" cy="118" r="104" fill="none" stroke="var(--grey)" stroke-width="4"/>
    <circle cx="640" cy="118" r="96" fill="none" stroke="var(--orange)" stroke-width="8"/>
  </svg>

  <div class="brand">LUMORA</div>

  <h1 class="headline">
    <span class="headline__name">Lumora Kids</span>
    <span class="headline__sub">Clothing</span>
  </h1>

  <ul class="needs">
    <li>Has sensitive skin due to medication</li>
    <li>Has a burn or scar that is not sun friendly</li>
    <li>Is sensitive to uncomfortable clothes<br>Or Is UV sensitive</li>
    <li>Then we might be able to help</li>
  </ul>

  <p class="intro">Our Little Lumora range is 100% Australian made bamboo jersey made especially for everyday sun protection</p>

  <div class="footer">www.lumora-wear.com</div>
</section>

<section class="card card--back">
  <svg class="card__art" width="768" height="547" viewBox="0 0 768 547">
    <defs>
      <linearGradient id="backScene" x1="0" y1="0" x2="0" y2="1">
        <stop offset="0" stop-color="var(--sky)"/>
        <stop offset=".55" stop-color="var(--sky-deep)"/>
        <stop offset=".78" stop-color="#b7a5d2"/>
        <stop offset=".9" stop-color="#d8c2b4"/>
        <stop offset="1" stop-color="var(--sand)"/>
      </linearGradient>
      <linearGradient id="studioNavy" x1="0" y1="0" x2="0" y2="1">
        <stop offset="0" stop-color="#f2f2f2"/><stop offset=".5" stop-color="#d9dce4"/><stop offset="1" stop-color="#2d3b5c"/>
      </linearGradient>
      <linearGradient id="studioBlue" x1="0" y1="0" x2="0" y2="1">
        <stop offset="0" stop-color="#f2f2f2"/><stop offset=".5" stop-color="#c9d8e6"/><stop offset="1" stop-color="#8fa9c6"/>
      </linearGradient>
      <linearGradient id="studioPurple" x1="0" y1="0" x2="0" y2="1">
        <stop offset="0" stop-color="#f2f2f2"/><stop offset=".45" stop-color="#c8c3e3"/><stop offset="1" stop-color="#7d78c0"/>
      </linearGradient>
      <linearGradient id="studioAqua" x1="0" y1="0" x2="0" y2="1">
        <stop offset="0" stop-color="#f2f2f2"/><stop offset=".5" stop-color="#c6e6ea"/><stop offset="1" stop-color="#8ecfd8"/>
      </linearGradient>
      <clipPath id="c1"><circle cx="482" cy="98" r="60"/></clipPath>
      <clipPath id="c2"><circle cx="682" cy="202" r="60"/></clipPath>
      <clipPath id="c3"><circle cx="449" cy="316" r="60"/></clipPath>
      <clipPath id="c4"><circle cx="697" cy="430" r="60"/></clipPath>
    </defs>
    <g role="img" aria-label="Three children in pastel bamboo outfits holding balloons on the beach">
      <path d="M0 0 H392 C372 150 282 330 0 392 Z" fill="url(#backScene)"/>
    </g>
    <path d="M402 -5 C382 160 292 346 -5 404" fill="none" stroke="var(--orange)" stroke-width="16"/>
    <path d="M424 -5 C402 170 306 362 -5 416" fill="none" stroke="var(--grey)" stroke-width="6"/>

    <g role="img" aria-label="Boy wearing a navy hooded top with high neckline" clip-path="url(#c1)">
      <rect x="420" y="36" width="124" height="124" fill="url(#studioNavy)"/>
    </g>
    <circle cx="482" cy="98" r="70" fill="none" stroke="var(--grey)" stroke-width="4"/>
    <circle cx="482" cy="98" r="63" fill="none" stroke="var(--orange)" stroke-width="7"/>

    <g role="img" aria-label="Girl wearing a light blue long sleeve top" clip-path="url(#c2)">
      <rect x="620" y="140" width="124" height="124" fill="url(#studioBlue)"/>
    </g>
    <circle cx="682" cy="202" r="70" fill="none" stroke="var(--grey)" stroke-width="4"/>
    <circle cx="682" cy="202" r="63" fill="none" stroke="var(--orange)" stroke-width="7"/>

    <g role="img" aria-label="Girl wearing a purple tunic with thumb loops" clip-path="url(#c3)">
      <rect x="387" y="254" width="124" height="124" fill="url(#studioPurple)"/>
    </g>
    <circle cx="449" cy="316" r="70" fill="none" stroke="var(--grey)" stroke-width="4"/>
    <circle cx="449" cy="316" r="63" fill="none" stroke="var(--orange)" stroke-width="7"/>

    <g role="img" aria-label="Girl wearing a breathable aqua printed outfit" clip-path="url(#c4)">
      <rect x="635" y="368" width="124" height="124" fill="url(#studioAqua)"/>
    </g>
    <circle cx="697" cy="430" r="70" fill="none" stroke="var(--grey)" stroke-width="4"/>
    <circle cx="697" cy="430" r="63" fill="none" stroke="var(--orange)" stroke-width="7"/>
  </svg>

  <h2 class="features-title">Features</h2>
  <div class="feature feature--necklines">High necklines</div>
  <div class="feature feature--sleeves">Long sleeves</div>
  <div class="feature feature--loops">Thumb loops for hand cover</div>
  <div class="feature feature--fabrics">Breathable fabrics</div>

  <p class="testing">Tested by RADSAFE to UPF 50+protection, we have your head, arms, legs and hands covered for every-day life outside<br>Life is for living, bring back fresh air and flowers in clothes from <span class="testing__link">lumora-wear.com</span></p>

  <div class="footer">www.lumora-wear.com</div>
</section>

</body>
</html>
```